Logo design and Businesscard and letterhead for Technology Company

We need logo design for a new company based in Atlanta called "Vornimel". We provide information about technology Product and service provider companies, information about their Products and services. Our initial focus is to List various companies and their products, various consulting companies and their services. We want to convey the message that this will be one stop shop to find out all the information to make smart technology decisions

I am looking for Logo, Business Card and Letterhead.

Target Market(s)

Companies that have IT department, IT users such as Developers, Managers, C level, Technology Product companies , Consulting companies and service providers.

Industry/Entity Type

It Company

Requirements
Must have
• Looking for some Unique design idea.
Nice to have
• I want something that connects information across technologies between technology buyers and sellers.
Should not have
• No puzzle design.

```html
<!DOCTYPE html>
<html lang="en">
<head>
<meta charset="utf-8">
<title>Vornimel – Brand Identity</title>
<link href="https://fonts.googleapis.com/css2?family=Lexend:wght@400;500;600&display=swap" rel="stylesheet">
<style>
  :root {
    --navy: #14287a;
    --navy-deep: #0b1a5c;
    --blue: #1f4fb8;
    --blue-light: #3f8fe0;
    --lime: #8cc21c;
    --white: #ffffff;
    --grey-line: #c9c9c9;
    --shadow: rgba(0,0,0,0.18);
    --font: "Lexend", "Helvetica Neue", Arial, sans-serif;
  }
  * { box-sizing: border-box; margin: 0; padding: 0; }
  html, body { width: 1200px; height: 805px; overflow: hidden; background: var(--white); font-family: var(--font); }
  .sheet { position: relative; width: 1200px; height: 805px; }

  .mark {
    position: absolute; border-radius: 50%;
    background: radial-gradient(circle at 35% 35%, var(--blue-light), var(--blue) 55%, var(--navy-deep));
  }
  .mark-shadow {
    position: absolute; height: 8px; border-radius: 50%;
    background: radial-gradient(ellipse, var(--shadow), transparent 70%);
  }
  .wordmark { position: absolute; font-weight: 500; color: var(--lime); line-height: 1; letter-spacing: -0.02em; white-space: nowrap; }
  .tagline { position: absolute; font-weight: 500; color: var(--navy); white-space: nowrap; line-height: 1; }

  .band {
    position: absolute; overflow: hidden;
    background: linear-gradient(100deg, var(--navy-deep) 0%, var(--blue) 45%, var(--navy) 70%, var(--navy-deep) 100%);
  }
  .band svg.swoosh { position: absolute; inset: 0; width: 100%; height: 100%; }
  .band .tagline { color: var(--white); }

  /* Letterhead */
  .letterhead { position: absolute; left: 35px; top: 29px; width: 573px; height: 743px; border: 1px solid var(--grey-line); }
  .letterhead-footer { left: 0; bottom: 0; width: 100%; height: 95px; }
  .contact-block { position: absolute; right: 14px; top: 8px; text-align: right; color: var(--white); font-size: 9.5px; font-weight: 600; line-height: 14.2px; }
  .contact-block .label { color: var(--lime); }

  /* Business cards */
  .card { position: absolute; width: 240px; height: 146px; border-radius: 10px; overflow: hidden; }
  .card-front { left: 652px; top: 554px; border: 1px solid var(--grey-line); background: var(--white); }
  .card-back { left: 928px; top: 554px; }
  .holder-name { position: absolute; left: 22px; top: 92px; font-size: 10px; font-weight: 600; color: var(--navy); }
  .holder-role { position: absolute; left: 22px; top: 104px; font-size: 7px; color: var(--lime); }
  .card-contact { position: absolute; left: 128px; top: 68px; font-size: 8px; color: var(--navy); line-height: 15px; font-weight: 500; }
  .card-contact .label { color: var(--lime); display: inline-block; width: 18px; }
  .card-url { position: absolute; left: 97px; top: 66px; font-size: 10px; font-weight: 600; color: var(--lime); }
</style>
</head>
<body>
<main class="sheet">

  <!-- Letterhead -->
  <section class="letterhead">
    <div class="mark" style="left:252px; top:18px; width:66px; height:66px;" role="img" aria-label="Vornimel brand circle"></div>
    <div class="mark-shadow" style="left:255px; top:96px; width:60px;"></div>

    <div class="band letterhead-footer">
      <svg class="swoosh" viewBox="0 0 573 95" preserveAspectRatio="none" aria-hidden="true">
        <path d="M0 20 C150 0 320 60 573 10 L573 30 C330 75 150 20 0 45 Z" fill="#2c6fd0" opacity="0.35"/>
        <path d="M0 70 C180 40 360 95 573 60 L573 95 L0 95 Z" fill="#0a1650" opacity="0.4"/>
      </svg>
      <div class="mark" style="left:28px; top:16px; width:48px; height:48px;" role="img" aria-label="Vornimel brand circle"></div>
      <div class="wordmark" style="left:88px; top:20px; font-size:32px;">Vornimel</div>
      <div class="tagline" style="left:90px; top:52px; font-size:6.5px;">Information about Technology Products &amp; Services</div>
      <div class="contact-block">
        2718 Linden Crest Drive,<br>
        Atlanta, GA 30319<br>
        <span class="label">P:</span> (404) 555-0182<br>
        <span class="label">F:</span> (404) 555 0193<br>
        <span class="label">E:</span> info@vornimel.com<br>
        <span class="label">W:</span> www.vornimel.com
      </div>
    </div>
  </section>

  <!-- Banner -->
  <section class="band" style="left:652px; top:65px; width:517px; height:99px;">
    <svg class="swoosh" viewBox="0 0 517 99" preserveAspectRatio="none" aria-hidden="true">
      <path d="M0 60 C140 30 330 90 517 40 L517 99 L0 99 Z" fill="#0a1650" opacity="0.35"/>
      <path d="M180 0 C260 40 400 20 517 0 Z" fill="#3f8fe0" opacity="0.25"/>
    </svg>
    <div class="mark" style="left:30px; top:10px; width:72px; height:72px;" role="img" aria-label="Vornimel brand circle"></div>
    <div class="wordmark" style="left:118px; top:12px; font-size:52px;">Vornimel</div>
    <div class="tagline" style="left:140px; top:62px; font-size:8px;">Information about Technology Products &amp; Services</div>
  </section>

  <!-- Primary logo -->
  <section>
    <div class="mark" style="left:669px; top:196px; width:104px; height:104px;" role="img" aria-label="Vornimel brand circle"></div>
    <div class="mark-shadow" style="left:672px; top:316px; width:96px;"></div>
    <div class="wordmark" style="left:790px; top:198px; font-size:78px;">Vornimel</div>
    <div class="tagline" style="left:842px; top:274px; font-size:10.5px;">Information about Technology Products &amp; Services</div>
  </section>

  <!-- Symbol variants -->
  <section>
    <div class="mark" style="left:718px; top:364px; width:126px; height:126px; background:radial-gradient(circle at 35% 35%, #ffffff, #c9ccd4 60%, #9a9ea8);" role="img" aria-label="Vornimel brand circle, light version"></div>
    <div class="mark-shadow" style="left:722px; top:510px; width:118px;"></div>
    <div class="mark" style="left:966px; top:364px; width:126px; height:126px;" role="img" aria-label="Vornimel brand circle, blue version"></div>
    <div class="mark-shadow" style="left:970px; top:510px; width:118px;"></div>
  </section>

  <!-- Business card front -->
  <section class="card card-front">
    <div class="mark" style="left:68px; top:17px; width:34px; height:34px;" role="img" aria-label="Vornimel brand circle"></div>
    <div class="wordmark" style="left:108px; top:20px; font-size:24px;">Vornimel</div>
    <div class="tagline" style="left:110px; top:44px; font-size:4.2px;">Information about Technology Products &amp; Services</div>
    <div class="holder-name">Daniel HARPER</div>
    <div class="holder-role">Director</div>
    <div class="card-contact">
      2718 Linden Crest Drive,<br>
      Atlanta, GA 30319<br>
      <span class="label">P:</span>(404) 555-0182<br>
      <span class="label">F:</span>(404) 555 0193<br>
      <span class="label">E:</span>info@vornimel.com
    </div>
  </section>

  <!-- Business card back -->
  <section class="card band card-back">
    <svg class="swoosh" viewBox="0 0 240 146" preserveAspectRatio="none" aria-hidden="true">
      <path d="M0 30 C70 10 150 60 240 20 L240 45 C150 85 70 35 0 60 Z" fill="#3f8fe0" opacity="0.3"/>
      <path d="M0 110 C90 80 160 140 240 100 L240 146 L0 146 Z" fill="#0a1650" opacity="0.4"/>
    </svg>
    <div class="mark" style="left:24px; top:37px; width:66px; height:66px;" role="img" aria-label="Vornimel brand circle"></div>
    <div class="card-url">www.vornimel.com</div>
  </section>

</main>
</body>
</html>
```